Website Design for a flight comparison website kestrel skyways

m looking to build a flight quote website

The fields of the website should be

THE SITE WILL BE CALLED KESTREL SKYWAYS.

WHY USE KESTREL SKYWAYS

Widest choice of airfares on sale in the UK
Speak to an expert and take the stress out of
trawling the internet
Save your time and we will search for you
Our lowest airfare guarantee or fly for free
Let us customise the deal if you need flexibility

Ticket Type: Return / One Way

Class: Economy / Premium Economy / Business / First
From: AIRPORTS
To: AIRPORTS

Depart Date: dd/mm/yyyy
Return Date: dd/mm/yyyy

Adults:
Children:
Infants (under 2)

— NEXT PAGE—

-----------------------------------------------
Details of Lead Passenger

First Name:
Middle Name:
Surname:

DOB:

Address 1
Address 2
Town
County
Postcode

Email Adress:
Landline:
Mobile:
—————————————————————————

— NET PAGE —
Your Card Will Not Be Charged

Credit Card

16 digit
EXPIRY
CCV

DEBIT CARD
16 DIGIT
EXPIRY
CCV

SORT CODE
ACCOUNT NUMBER

—SUBMIT—

Thank you for using Kestrel Skyways.

Nothing needs to be too complicated just a one page website where users register their interest and then we will call them back offline.
Updates

Target Market(s)

People planning to travel last minute to all destinations worldwide.

Industry/Entity Type

Business

Requirements
Must have
• Be cool looking easy user interface.
Nice to have
• Parallax would be nice to make the site look modern and inline with todays websites.

```html
<!DOCTYPE html>
<html lang="en">
<head>
<meta charset="utf-8">
<title>Kestrel Skyways</title>
<link href="https://fonts.googleapis.com/css2?family=Lato:ital,wght@0,400;0,700;0,900;1,700;1,900&display=swap" rel="stylesheet">
<style>
:root{
  --navy:#2d3b4f;
  --navy-deep:#2a374a;
  --nav-text:#a7b3c4;
  --sky-top:#2f9be0;
  --sky-mid:#6cc2ef;
  --sea:#cde9f4;
  --promo-photo:#3a6f9e;
  --accent:#fbb615;
  --green:#8dc63f;
  --green-dark:#6fa82a;
  --blue-link:#29a9e0;
  --field:#f2f2f2;
  --field-text:#a8a8a8;
  --label:#555;
  --heading:#333;
  --tab:#eef0f2;
  --tab-text:#8a96a3;
  --band:#f0f1f2;
  --footer:#f2f3f4;
  --white:#fff;
}
*{box-sizing:border-box;margin:0;padding:0}
html,body{width:1200px;height:1183px;overflow:hidden}
body{position:relative;font-family:'Lato',sans-serif;background:var(--white);color:var(--heading)}

/* header */
.site-header{position:absolute;left:0;top:0;width:1200px;height:75px;background:var(--navy)}
.brand{position:absolute;display:flex;align-items:center;gap:10px;font-weight:700;font-size:23px;color:var(--white)}
.brand-dot{width:30px;height:22px;border-radius:50%;background:var(--accent)}
.site-header .brand{left:92px;top:21px}
.main-nav a{position:absolute;top:28px;font-size:10.5px;font-weight:700;letter-spacing:.2px;color:var(--nav-text);text-decoration:none;text-transform:uppercase}
.main-nav a.current{color:var(--white)}
.social span{position:absolute;top:29px;width:9px;height:9px;border-radius:50%;background:var(--nav-text)}

/* hero */
.hero{position:absolute;left:0;top:75px;width:1200px;height:562px}
.hero-photo{position:absolute;inset:0;
  background:linear-gradient(180deg,var(--sky-top) 0%,var(--sky-mid) 50%,#a9dcf3 78%,var(--sea) 100%)}
.hero-copy{position:absolute;left:112px;top:155px;color:var(--white)}
.hero-copy h1{font-size:26px;font-weight:400;line-height:36px;margin-bottom:3px}
.hero-copy h1 em{font-weight:900;font-style:italic}
.perks{list-style:none}
.perks li{display:flex;align-items:center;gap:18px;font-size:21px;height:37px}
.perks li b{font-weight:700;font-size:18px}
.perks svg{width:22px;height:22px;flex:none}
.btn-more{position:absolute;left:116px;top:357px;width:140px;height:30px;background:var(--navy);color:var(--white);
  font-size:14px;font-weight:700;display:flex;align-items:center;justify-content:center}
.tabs{position:absolute;left:90px;top:527px;display:flex;gap:2px}
.tabs span{height:35px;display:flex;align-items:center;justify-content:center;font-size:10.5px;font-weight:700;letter-spacing:.3px;background:var(--tab);color:var(--tab-text)}
.tabs span.active{background:var(--white);color:var(--blue-link)}

/* search form */
.search-form{position:absolute;left:0;top:637px;width:1200px;height:211px;background:var(--white)}
.group-title{position:absolute;top:36px;font-size:14px;color:var(--heading)}
.field-label{position:absolute;font-size:9.5px;font-weight:700;color:var(--label);text-transform:uppercase;letter-spacing:.2px}
.field{position:absolute;height:30px;background:var(--field);font-size:10px;color:var(--field-text);display:flex;align-items:center;padding-left:13px}
.field.value{color:#666}
.field .knob{position:absolute;right:0;top:0;height:30px;background:var(--accent);display:flex;align-items:center;justify-content:center}
.knob.cal{width:26px}
.knob.drop{width:20px}
.knob.drop i{display:block;width:6px;height:4px;border-top:1px solid #fff;border-bottom:1px solid #fff}
.btn-next{position:absolute;left:955px;top:143px;width:155px;height:30px;background:var(--green);color:var(--white);font-size:10px;font-weight:700;display:flex;align-items:center;padding-left:52px}
.btn-next .tick{position:absolute;right:0;top:0;width:26px;height:30px;background:var(--green-dark);display:flex;align-items:center;justify-content:center}

.spacer-band{position:absolute;left:0;top:848px;width:1200px;height:72px;background:var(--band)}

/* promo band */
.promo{position:absolute;left:0;top:920px;width:1200px;height:217px;background:var(--navy-deep)}
.promo-photo{position:absolute;left:40px;top:12px;width:252px;height:205px;
  background:linear-gradient(180deg,var(--navy-deep) 0%,var(--promo-photo) 100%)}
.promo-text{position:absolute;left:345px;top:80px;color:var(--white)}
.promo-text p{font-size:21px;font-weight:400}
.promo-text h2{font-size:27px;font-weight:700;margin-top:4px}
.promo-input{position:absolute;left:855px;top:70px;width:255px;height:38px;background:var(--white);font-size:12px;color:var(--field-text);display:flex;align-items:center;padding-left:13px}
.promo-btn{position:absolute;left:855px;top:116px;width:255px;height:38px;background:var(--green);color:var(--white);font-size:12px;font-weight:700;display:flex;align-items:center;justify-content:center}

/* footer */
.site-footer{position:absolute;left:0;top:1137px;width:1200px;height:46px;background:var(--footer)}
.site-footer .brand{left:92px;top:12px;color:var(--navy)}
.footer-links{position:absolute;right:133px;top:23px;font-size:12px;color:#666}
.to-top{position:absolute;left:1085px;top:18px;width:25px;height:25px;border:1px solid var(--blue-link);border-radius:50%;display:flex;align-items:center;justify-content:center}
</style>
</head>
<body>

<header class="site-header">
  <div class="brand"><span class="brand-dot"></span>Kestrel Skyways</div>
  <nav class="main-nav">
    <a class="current" style="left:464px">Home</a>
    <a style="left:534px">Flight Search</a>
    <a style="left:655px">About Us</a>
    <a style="left:747px">Contact Us</a>
    <a style="left:852px">Login</a>
    <a style="left:922px">Sign Up</a>
  </nav>
  <div class="social">
    <span style="left:994px"></span><span style="left:1025px"></span><span style="left:1057px"></span><span style="left:1089px"></span>
  </div>
</header>

<section class="hero">
  <div class="hero-photo" role="img" aria-label="Sky and sea with a tropical island, an airliner and a flight attendant in blue uniform saluting"></div>
  <div class="hero-copy">
    <h1>Let’s <em>Discover</em> the world together!</h1>
    <ul class="perks">
      <li><svg viewBox="0 0 24 24"><path d="M2 15l20-6-6 5 3 1-2 1-5-1-8 2z" fill="#fff"/></svg><span>Over <b>500</b> Airlines</span></li>
      <li><svg viewBox="0 0 24 24"><path d="M3 21V8h5v13M9 21V3h6v18M16 21v-9h5v9z" fill="#fff"/></svg><span>More than <b>13,000</b> Places</span></li>
      <li><svg viewBox="0 0 24 24"><circle cx="12" cy="12" r="8" fill="none" stroke="#fff" stroke-width="2"/><path d="M8 12l3 3 5-6" fill="none" stroke="#fff" stroke-width="2"/></svg><span>Best Price Guarantee</span></li>
      <li><svg viewBox="0 0 24 24"><circle cx="12" cy="9" r="4.5" fill="#fff"/><path d="M4 20c0-5 16-5 16 0z" fill="#fff"/></svg><span>Customer Care</span></li>
    </ul>
  </div>
  <div class="btn-more">FINE OUT MORE</div>
  <div class="tabs">
    <span class="active" style="width:143px">FLIGHTS SEARCH</span>
    <span style="width:135px">FLIGHT STATUS</span>
    <span style="width:149px">ONLINE CHECK IN</span>
  </div>
</section>

<section class="search-form">
  <div class="group-title" style="left:90px">Where</div>
  <div class="group-title" style="left:436px">When</div>
  <div class="group-title" style="left:782px">Who</div>

  <div class="field-label" style="left:90px;top:63px">Leaving From</div>
  <div class="field" style="left:90px;top:80px;width:328px">city, district or specific airpot</div>
  <div class="field-label" style="left:90px;top:126px">Going To</div>
  <div class="field" style="left:90px;top:143px;width:328px">city, district or specific airpot</div>

  <div class="field-label" style="left:436px;top:63px">Departing On</div>
  <div class="field" style="left:436px;top:80px;width:156px">mm/dd/yy<span class="knob cal"><svg width="12" height="11" viewBox="0 0 12 11"><rect x=".5" y="1.5" width="11" height="9" fill="none" stroke="#fff"/><path d="M.5 4h11M3 6h6M3 8h6" stroke="#fff"/></svg></span></div>
  <div class="field value" style="left:609px;top:80px;width:155px;padding-left:8px">anytime<span class="knob drop"><i></i></span></div>
  <div class="field-label" style="left:436px;top:126px">Arriving On</div>
  <div class="field" style="left:436px;top:143px;width:156px">mm/dd/yy<span class="knob cal"><svg width="12" height="11" viewBox="0 0 12 11"><rect x=".5" y="1.5" width="11" height="9" fill="none" stroke="#fff"/><path d="M.5 4h11M3 6h6M3 8h6" stroke="#fff"/></svg></span></div>
  <div class="field value" style="left:609px;top:143px;width:155px;padding-left:8px">anytime<span class="knob drop"><i></i></span></div>

  <div class="field-label" style="left:782px;top:63px">Adults</div>
  <div class="field value" style="left:782px;top:80px;width:69px;padding-left:9px">01<span class="knob drop"><i></i></span></div>
  <div class="field-label" style="left:868px;top:63px">Kids</div>
  <div class="field value" style="left:868px;top:80px;width:69px;padding-left:9px">01<span class="knob drop"><i></i></span></div>
  <div class="field-label" style="left:955px;top:63px">Promo Code</div>
  <div class="field" style="left:955px;top:80px;width:155px">type here</div>
  <div class="field-label" style="left:782px;top:126px">Infants</div>
  <div class="field value" style="left:782px;top:143px;width:69px;padding-left:9px">01<span class="knob drop"><i></i></span></div>

  <div class="btn-next">NEXT<span class="tick"><svg width="12" height="10" viewBox="0 0 12 10"><path d="M1 5l3.5 3.5L11 1" fill="none" stroke="#fff" stroke-width="2"/></svg></span></div>
</section>

<div class="spacer-band"></div>

<section class="promo">
  <div class="promo-photo" role="img" aria-label="Flight attendant in blue uniform saluting"></div>
  <div class="promo-text">
    <p>Comfortable and modern flight experience.</p>
    <h2>400+ Airlines to Travel The World!</h2>
  </div>
  <div class="promo-input">Enter destination or hotel name</div>
  <div class="promo-btn">SEARCH FLIGHTS</div>
</section>

<footer class="site-footer">
  <div class="brand"><span class="brand-dot"></span>Kestrel Skyways</div>
  <div class="footer-links">Home | About | Privacy Policy | Term of Use | © 2014 Kestrel Skyways</div>
  <div class="to-top"><svg width="8" height="10" viewBox="0 0 8 10"><path d="M4 9V1M1 4l3-3 3 3" fill="none" stroke="#2d3b4f" stroke-width="1.2"/></svg></div>
</footer>

</body>
</html>
```